Valdarossi’s Artisan Pizzeria Menu Contest

I’m looking for a menu design for a new pizzeria - it’s farm to table type of restaurant - more upscale than a typical pizzeria - white washed wood interior with some industrial accents - I am looking for a creative menu layout using the attached sample menu items -
Valdarossi’s is an artisanal pizzeria with an atmosphere that will make you feel at home for any situation, first date, anniversary, business lunch, boys night out or girls night out with a menu inspired by the idea of a simple honest cooking paired with fresh – quality ingredients. Full service dining experience that is still casual but dedicated to extraordinary hospitality.
While developing the menu we have created a network of amazing farms and purveyors to supply our restaurant with fresh milled 100% California flour for our hand crafted dough, as well as sustainably farmed organic produce, meats and cheeses.
The menu includes classics like the Margherita pizza to daily seasonal specials, fresh salads to rustic small plates including moms meatball recipe to a fresh local burrata with handmade bread. Each dish reflects our passion for sourcing the freshest quality local ingredients.
To compliment the menu, Valdarossi’s serves an extensive wine list with selections focusing on Italian varietals. The cocktail program has been carefully crafted to offer something to entice ever palate and the beer list has unique selections of the world’s finest brewers.
Target Market(s)
25-45 year old men and women
Industry/Entity Type
American Restaurant
Requirements
Must have
- professional tone
Nice to have
- a balance of elegance and industrial (rustic)
Should not have
- photos or playful graphics etc..

```html
<!DOCTYPE html>
<html lang="en">
<head>
<meta charset="utf-8">
<title>Valdarossi’s Artisan Pizzeria Menu</title>
<link href="https://fonts.googleapis.com/css2?family=Sorts+Mill+Goudy&family=Cormorant+SC:wght@600;700&display=swap" rel="stylesheet">
<style>
  :root{
    --ink:#5b4a3d;
    --ink-soft:#6a594b;
    --paper-1:#f4f1ec;
    --paper-2:#e6e1d8;
    --paper-3:#d7d0c4;
    --veil:rgba(255,255,255,0.72);
  }
  *{box-sizing:border-box;margin:0;padding:0}
  html,body{width:1200px;height:729px;overflow:hidden}
  body{position:relative;background:var(--paper-1);color:var(--ink);font-family:"Sorts Mill Goudy",Georgia,serif}
  .backdrop{position:absolute;inset:0;
    background:
      radial-gradient(ellipse at 30% 45%, rgba(255,255,255,.9), rgba(255,255,255,0) 60%),
      linear-gradient(180deg,var(--paper-1) 0%,var(--paper-2) 55%,var(--paper-3) 100%);}
  .veil{position:absolute;left:412px;top:0;right:0;bottom:0;background:var(--veil)}
  .brand{position:absolute;left:22px;top:56px;width:250px;text-align:center}
  .brand-name{font-size:40px;color:var(--ink);letter-spacing:1px;line-height:1}
  .brand-sub{font-size:14px;letter-spacing:3px;margin-top:6px;color:var(--ink)}
  .heading{position:absolute;font-family:"Cormorant SC",Georgia,serif;font-weight:700;font-size:27px;line-height:1;color:var(--ink)}
  .item{position:absolute;width:158px}
  .item-name{font-size:20px;line-height:1;color:var(--ink);margin-bottom:2px}
  .item-desc{font-size:13px;line-height:17px;color:var(--ink-soft)}
  .price{font-size:18px;color:var(--ink);white-space:nowrap}
  .price-inline{font-family:"Sorts Mill Goudy",Georgia,serif;font-weight:400}
  .wide{width:330px}
</style>
</head>
<body>
<div class="backdrop" role="img" aria-label="Softly faded view of a white-washed restaurant dining room"></div>
<div class="veil"></div>

<header class="brand">
  <div class="brand-name">VALDAROSSI’S</div>
  <div class="brand-sub">ARTISAN PIZZERIA</div>
</header>

<!-- Appetizers -->
<h2 class="heading" style="left:17px;top:214px">Appetizer’s</h2>
<div class="item" style="left:17px;top:244px"><div class="item-name">Brussels</div><div class="item-desc">Pan seared brussel sprouts with a drizzle of balsamic reduction with parm and bread crumbs <span class="price">$10</span></div></div>
<div class="item" style="left:17px;top:375px"><div class="item-name">Mussels</div><div class="item-desc">New Zealand mussel’s in a tomato broth <span class="price">$15</span></div></div>
<div class="item" style="left:17px;top:453px"><div class="item-name">Chicken Wings</div><div class="item-desc">Italian fried chicken wings with a kick <span class="price">$10</span></div></div>
<div class="item" style="left:185px;top:244px"><div class="item-name">Meatballs</div><div class="item-desc">Mom’s secret handmade meatball recipe for over 75 years <span class="price">$13</span></div></div>
<div class="item" style="left:185px;top:339px"><div class="item-name">Romanesco</div><div class="item-desc">Flash fried romanesco served atop a spicy aioli <span class="price">$11</span></div></div>
<div class="item" style="left:185px;top:436px"><div class="item-name">Burrata</div><div class="item-desc">Local burrata served with apples, grapes, and freshly made bread <span class="price">$13</span></div></div>
<div class="heading" style="left:14px;top:580px;font-size:24px">Daily Soup <span class="price price-inline">$8</span></div>
<div class="item wide" style="left:14px;top:605px"><div class="heading" style="position:static;font-size:24px">Dips <span class="price price-inline">$1</span></div><div class="item-desc">Ranch, tomato sauce, spicy dip, blue cheese</div></div>

<!-- Salads -->
<h2 class="heading" style="left:423px;top:12px">Salad’s</h2>
<div class="item" style="left:423px;top:40px"><div class="item-name">Chopped Salad</div><div class="item-desc">Lettuce mix with tomato, onions, peppers, pepperoni, chick peas, fresh mozz, italian herb vinagrette <span class="price">$13</span></div></div>
<div class="item" style="left:423px;top:164px"><div class="item-name">Farm Salad</div><div class="item-desc">Seasonal farmers market salad <span class="price">$15</span></div></div>
<div class="item" style="left:423px;top:228px"><div class="item-name">Spinach &amp; Arugula</div><div class="item-desc">Spinach and argula, red pepperstossed in a lemon ving and housemade croutons <span class="price">$12</span></div></div>
<div class="item" style="left:593px;top:40px"><div class="item-name">Caeser Salad</div><div class="item-desc">Traditional caesar salad, rich and creamy, extra shaved parmesan <span class="price">$11</span></div></div>
<div class="item" style="left:593px;top:127px"><div class="item-name">Grilled Little Gem</div><div class="item-desc">Grilled little gems with bacon, tomato, red onions and blue cheese dressing <span class="price">$11</span></div></div>

<!-- Sandwiches -->
<h2 class="heading" style="left:423px;top:366px">Sandwiches</h2>
<div class="item" style="left:425px;top:394px"><div class="item-name">Italian Sub</div><div class="item-desc">Prociutto, salumi, turkey, provolone, lettuce, tomato and herb aioli with spicy gardenia <span class="price">$13</span></div></div>
<div class="item" style="left:425px;top:519px"><div class="item-name">Meatball Sub</div><div class="item-desc">Mom’s meatballs, melted provolone on a housemade roll <span class="price">$13</span></div></div>
<div class="item" style="left:425px;top:599px"><div class="item-name">Chicken Sandwich</div><div class="item-desc">Spinach and argula, red pepperstossed in a lemon ving and housemade croutons <span class="price">$12</span></div></div>
<div class="item" style="left:594px;top:394px"><div class="item-name">Turkey Sandwich</div><div class="item-desc">Housemade bread, turkey, cheddar cheese, butter lettuce, tomato and mustard aioli <span class="price">$12</span></div></div>
<div class="item" style="left:594px;top:524px"><div class="item-name">Plantfield Burger</div><div class="item-desc">Arugula, tomato, onion, and a sundried tomato spread on a housemade bun <span class="price">$14</span></div></div>

<!-- Pizzas -->
<h2 class="heading" style="left:823px;top:12px">Pizza’s</h2>
<div class="item" style="left:823px;top:42px"><div class="item-name">Margherita</div><div class="item-desc">Classic Margherita pizza - Fresh Mozz, Tomato Sauce, and Basil <span class="price">$14</span></div></div>
<div class="item" style="left:823px;top:121px"><div class="item-name">Organic Sausage</div><div class="item-desc">Organic Sausage House-made red sauce, mozz, and a hint of fennel <span class="price">$16</span></div></div>
<div class="item" style="left:823px;top:244px"><div class="item-name">Spinach &amp; Arugula</div><div class="item-desc">Spinach and argula, red pepperstossed in a lemon ving and housemade croutons <span class="price">$12</span></div></div>
<div class="item" style="left:823px;top:370px"><div class="item-name">Prosciutto &amp; Egg</div><div class="item-desc">Parma, Prosciutto, Parmesan cream with Alpenhof and gruyere, finished with an organic egg <span class="price">$16</span></div></div>
<div class="item" style="left:823px;top:518px"><div class="item-name">Farmer’s Pizza</div><div class="item-desc">Seasonal vegetables, cream sauce, and a variety of cheeses <span class="price">$17</span></div></div>
<div class="item" style="left:994px;top:42px"><div class="item-name">Pepperoni</div><div class="item-desc">Harlow pepperoni - housemade red sauce, chile flakes, and mozz <span class="price">$16</span></div></div>
<div class="item" style="left:994px;top:136px"><div class="item-name">Salumi &amp; Burrati</div><div class="item-desc">Salumi dried, red sauce finished with whipped burrata <span class="price">$17</span></div></div>
<div class="item" style="left:994px;top:246px"><div class="item-name">Daily Special <span class="price" style="font-size:20px">$17</span></div><div class="item-name">Mushroom</div><div class="item-desc">Shaved mushrooms with a parmesan cream and melted onions <span class="price">$16</span></div></div>
<div class="item" style="left:994px;top:351px"><div class="item-name">Quattro Formaggi</div><div class="item-desc">Four cheese combination - mozz - fontina - parm cream and gruyere chile flakes and oregano <span class="price">$15</span></div></div>
<div class="item" style="left:994px;top:482px"><div class="item-name">Keto Friendly</div><div class="item-desc">Cauliflower crust, spinach and kale , parm cream sauce <span class="price">$17</span></div></div>

<!-- Crusts -->
<h2 class="heading" style="left:823px;top:599px">Crust’s</h2>
<div class="item" style="left:823px;top:624px"><div class="item-name">Traditional</div><div class="item-desc">Orginal crust you can’t miss</div></div>
<div class="item" style="left:823px;top:684px"><div class="item-name">Cauliflower</div><div class="item-desc">Vegans have needs <span class="price">$3</span></div></div>
<div class="item" style="left:994px;top:627px"><div class="item-name">Gluten-Free</div><div class="item-desc">Best gluten friendly crust on the west coast <span class="price">$3</span></div></div>
</body>
</html>
```